ALL TEXT GRAPHICS TM May 2025 for Instagram

We are looking for a series of social media graphics for Instagram (new size: 4:5 (1080 x 1350 pixels) ratio that are ALL TEXT. We want the following quotes below on each graphic; one quote per graphic. AND, In very small letters at the bottom of each graphic, add @TovaMarshOnline
The look and feel of these graphics should be complimentary to the color palette attached below; but keep them simple. But the design is up to you; at the end of this document, I provided various samples of all text graphics that I like as examples.
Target Market(s)
women looking to lose weight
Look and feel

```html
<!DOCTYPE html>
<html lang="en">
<head>
<meta charset="utf-8">
<title>Instagram text graphics — Tova Marsh</title>
<link rel="stylesheet" href="https://fonts.googleapis.com/css2?family=Alfa+Slab+One&family=Anton&family=Archivo+Black&family=Bangers&family=Great+Vibes&family=Lobster&family=Poppins:wght@500;700;800;900&display=swap">
<style>
:root{
  --pink:#ff0a84;
  --pink-soft:#ff3a9c;
  --yellow:#ffe100;
  --ink:#111111;
  --white:#ffffff;
  --stage:#d9d9d9;
}
*{margin:0;padding:0;box-sizing:border-box}
html,body{width:1007px;height:1200px;overflow:hidden;background:var(--stage)}
.board{position:relative;width:1007px;height:1200px}
.post{position:absolute;width:409px;height:511px;background:var(--white);overflow:hidden}
.post--a{left:83px;top:75px}
.post--b{left:521px;top:75px}
.post--c{left:83px;top:615px}
.post--d{left:521px;top:615px}
.pink-field{position:absolute;left:0;right:0;top:0;background:
  radial-gradient(ellipse 120% 90% at 110% 110%, var(--pink-soft) 0 30%, transparent 31%),
  radial-gradient(ellipse 90% 120% at -20% 80%, var(--pink-soft) 0 35%, transparent 36%),
  var(--pink)}
.frame{position:absolute;border:1.5px solid #333}
.line{position:absolute;left:0;right:0;text-align:center;white-space:nowrap}
.handle{font-family:"Poppins",sans-serif;font-weight:500;font-size:12px;color:var(--ink)}
.handle--light{color:var(--white)}

/* Post A */
.post--a .frame{left:18px;top:17px;width:374px;height:240px;border-bottom:none}
.post--a .pink-field{top:235px;bottom:0}
.stack-word{font-family:"Archivo Black",sans-serif;color:var(--pink);text-shadow:-3px 3px 0 var(--ink);letter-spacing:-1px;line-height:1}
.stack-word--tired{top:24px;font-size:68px}
.stack-word--moody{top:96px;font-size:73px}
.stack-word--stubborn{top:172px;font-size:50px}
.battery{display:inline-block;width:26px;height:56px;vertical-align:-2px;margin:0 2px}
.script-title{top:236px;font-family:"Lobster",sans-serif;font-size:88px;color:var(--white);text-shadow:-3px 3px 0 var(--ink);line-height:1}
.script-sub{font-family:"Great Vibes",cursive;font-size:46px;color:var(--white);line-height:1}
.script-sub--1{top:336px}
.script-sub--2{top:384px}
.cta-box{position:absolute;left:120px;top:438px;width:167px;height:30px;background:var(--white);font-family:"Poppins",sans-serif;font-weight:700;font-size:16px;color:var(--ink);text-align:center;line-height:30px}
.post--a .handle{top:476px}

/* Post B */
.post--b .pink-field{height:386px}
.post--b .frame{left:18px;top:386px;width:374px;height:105px;border-top:none}
.condensed{font-family:"Anton",sans-serif;line-height:1}
.headline-top{top:36px;font-size:50px;color:var(--white)}
.weight-row{top:100px;display:flex;justify-content:center;align-items:center;gap:8px}
.weight-word{font-family:"Anton",sans-serif;font-size:60px;color:var(--yellow);text-shadow:-3px 3px 0 var(--ink);line-height:1}
.dumbbell{width:44px;height:66px}
.fault-banner{position:absolute;left:15px;top:187px;width:377px;height:60px}
.fault-text{top:196px;font-family:"Anton",sans-serif;font-size:34px;color:var(--pink);line-height:1}
.fault-text .big{font-size:42px;vertical-align:-4px}
.marker-line{font-family:"Bangers",sans-serif;font-size:27px;color:var(--white);letter-spacing:1px;transform:skewX(-10deg);line-height:1}
.marker-line--1{top:278px}
.marker-line--2{top:318px}
.fix-line{top:398px;font-family:"Poppins",sans-serif;font-weight:800;font-size:33px;color:var(--ink)}
.post--b .handle{top:466px}

/* Post C */
.post--c .pink-field{height:335px}
.post--c .frame{left:18px;top:335px;width:374px;height:159px;border-top:none}
.bold-caps{font-family:"Poppins",sans-serif;font-weight:800;color:var(--white);line-height:1}
.belly-line{top:34px;font-size:45px;letter-spacing:-1px}
.notfat-line{top:76px;font-family:"Poppins",sans-serif;font-weight:900;font-size:64px;color:var(--pink);-webkit-text-stroke:2px var(--white);letter-spacing:-1px;line-height:1}
.hormonal-box{position:absolute;left:26px;top:169px;width:357px;height:49px;background:var(--white);border-radius:6px;text-align:center;font-family:"Lobster",sans-serif;font-size:50px;color:var(--pink);line-height:44px;overflow:hidden}
.howto-line{font-size:31px;letter-spacing:-0.5px}
.howto-line--1{top:248px}
.howto-line--2{top:280px}
.comment-label{top:342px;font-family:"Poppins",sans-serif;font-weight:800;font-size:25px;color:var(--ink)}
.comment-pill{position:absolute;left:79px;top:374px;width:251px;height:43px;background:var(--pink);border-radius:10px 22px 10px 10px;font-family:"Poppins",sans-serif;font-weight:800;font-size:33px;color:var(--white);text-align:center;line-height:45px}
.working-line{top:427px;font-family:"Poppins",sans-serif;font-weight:800;font-size:25px;color:var(--ink)}
.post--c .handle{top:474px}

/* Post D */
.post--d .pink-field{height:393px}
.title-frame{position:absolute;left:22px;top:20px;width:364px;height:174px}
.post--d .frame{left:26px;top:393px;width:357px;height:95px;border-top:none}
.after-head{font-family:"Anton",sans-serif;font-size:39px;color:var(--white);text-align:left;left:54px;line-height:1}
.after-head--top{top:40px}
.after-head--bottom{top:154px}
.bellyfat-big{top:78px;left:54px;text-align:left;font-family:"Anton",sans-serif;font-size:82px;color:var(--yellow);text-shadow:-3px 3px 0 var(--ink);line-height:1}
.slab-line{font-family:"Alfa Slab One",serif;font-size:33px;color:var(--white);line-height:1}
.slab-line--1{top:216px}
.slab-line--2{top:252px}
.slab-line .accent{color:var(--yellow)}
.flame{display:inline-block;width:24px;height:32px;vertical-align:-3px}
.about-line{font-size:30px;letter-spacing:-0.5px}
.about-line--1{top:308px}
.about-line--2{top:339px}
.thefix-line{top:398px;font-family:"Poppins",sans-serif;font-weight:800;font-size:37px;color:var(--ink);letter-spacing:-0.5px}
.post--d .handle{top:458px}
</style>
</head>
<body>
<main class="board">

  <section class="post post--a">
    <div class="frame"></div>
    <div class="line stack-word stack-word--tired">T<svg class="battery" viewBox="0 0 26 56" aria-hidden="true"><rect x="8" y="1" width="10" height="5" fill="#111"/><rect x="2" y="5" width="22" height="49" rx="5" fill="#fff" stroke="#111" stroke-width="3"/><rect x="6" y="40" width="14" height="10" fill="#ff0a84"/></svg>RED</div>
    <div class="line stack-word stack-word--moody">MOODY</div>
    <div class="line stack-word stack-word--stubborn">STUBBORN</div>
    <div class="pink-field"></div>
    <div class="line script-title">Belly Fat</div>
    <div class="line script-sub script-sub--1">Your hormones are</div>
    <div class="line script-sub script-sub--2">screaming for help</div>
    <div class="cta-box">LET’S FIX THAT</div>
    <div class="line handle handle--light">@TovaMarshOnline</div>
  </section>

  <section class="post post--b">
    <div class="pink-field"></div>
    <div class="line condensed headline-top">THAT STUBBORN</div>
    <div class="line weight-row">
      <svg class="dumbbell" viewBox="0 0 44 66" aria-hidden="true"><rect x="0" y="22" width="10" height="22" fill="#ffe100"/><rect x="13" y="10" width="8" height="46" fill="#ffe100"/><rect x="25" y="0" width="14" height="66" fill="#ffe100"/></svg>
      <span class="weight-word">WEIGHT?</span>
      <svg class="dumbbell" viewBox="0 0 44 66" aria-hidden="true"><rect x="5" y="0" width="14" height="66" fill="#ffe100"/><rect x="23" y="10" width="8" height="46" fill="#ffe100"/><rect x="34" y="22" width="10" height="22" fill="#ffe100"/></svg>
    </div>
    <svg class="fault-banner" viewBox="0 0 377 60" aria-hidden="true"><polygon points="0,0 377,7 371,60 5,58" fill="#fff"/></svg>
    <div class="line fault-text">IT’S <span class="big">NOT</span> YOUR FAULT</div>
    <div class="line marker-line marker-line--1">YOUR HORMONES ARE TO</div>
    <div class="line marker-line marker-line--2">BLAME AND YOU’RE NOT ALONE</div>
    <div class="frame"></div>
    <div class="line fix-line">BUT THERE IS A FIX</div>
    <div class="line handle">@TovaMarshOnline</div>
  </section>

  <section class="post post--c">
    <div class="pink-field"></div>
    <div class="line bold-caps belly-line">YOUR BELLY IS</div>
    <div class="line notfat-line">NOT FAT...</div>
    <div class="hormonal-box">it’s hormonal</div>
    <div class="line bold-caps howto-line howto-line--1">AND HERE’S HOW TO</div>
    <div class="line bold-caps howto-line howto-line--2">FIX IT</div>
    <div class="frame"></div>
    <div class="line comment-label">COMMENT</div>
    <div class="comment-pill">HORMONES</div>
    <div class="line working-line">IF NOTHING IS WORKING</div>
    <div class="line handle">@TovaMarshOnline</div>
  </section>

  <section class="post post--d">
    <div class="pink-field"></div>
    <svg class="title-frame" viewBox="0 0 364 174" aria-hidden="true" fill="none" stroke="#fff" stroke-width="5"><polyline points="2,174 2,2 362,2 362,157 220,157"/></svg>
    <div class="line after-head after-head--top">THE STUBBORN</div>
    <div class="line bellyfat-big">BELLY FAT</div>
    <div class="line after-head after-head--bottom">AFTER 40?</div>
    <div class="line slab-line slab-line--1">IT’S <span class="accent">NOT</span> ABOUT</div>
    <div class="line slab-line slab-line--2">CAL<svg class="flame" viewBox="0 0 24 32" aria-hidden="true"><path d="M12 1C14 8 22 12 22 21a10 10 0 0 1-20 0c0-6 4-9 5-13 2 3 2 6 4 7 1-5 0-9 1-14z" fill="none" stroke="#fff" stroke-width="2.5"/><path d="M12 16c2 3 5 5 5 8a5 5 0 0 1-10 0c0-3 3-5 5-8z" fill="#fff"/></svg>RIES</div>
    <div class="line bold-caps about-line about-line--1">IT’S ABOUT YOUR</div>
    <div class="line bold-caps about-line about-line--2">HORMONES</div>
    <div class="frame"></div>
    <div class="line thefix-line">HERE IS THE FIX!</div>
    <div class="line handle">@TovaMarshOnline</div>
  </section>

</main>
</body>
</html>
```